Mirela Hastow ADHD coach needs a flyer

I need a flyer to be sent by email. the copy is attached. It can be changed/reduced to fit the flyer. I would like to keep my website colors. My website is www.mirelahastow.example - Thank you!

```html
<!DOCTYPE html>
<html lang="en">
<head>
<meta charset="utf-8">
<title>Mirela Hastow – Academic Success Coaching Flyer</title>
<link rel="stylesheet" href="https://fonts.googleapis.com/css2?family=Montserrat:ital,wght@0,300;0,400;0,500;0,600;0,700;0,800;1,500&family=Questrial&display=swap">
<style>
  :root {
    --blue: #89abb9;
    --slate: #77857f;
    --photo-light: #a3b2b5;
    --photo-dark: #7d9296;
    --paper-top: #f3f3f4;
    --paper-bottom: #e1e1e4;
    --ink: #4a4b4d;
    --ink-soft: #5a5b5e;
    --footer: #4b4c4e;
    --white: #ffffff;
    --bubble-light: #dcdde0;
    --bubble-white: #f4f4f5;
  }
  * { box-sizing: border-box; margin: 0; padding: 0; }
  html, body { width: 1070px; height: 1200px; overflow: hidden; }
  body {
    position: relative;
    font-family: "Questrial", "Helvetica Neue", Arial, sans-serif;
    color: var(--ink);
    background: linear-gradient(180deg, var(--paper-top) 0%, var(--paper-bottom) 100%);
  }

  /* Hero */
  .hero { position: absolute; left: 0; top: 0; width: 1070px; height: 590px; background: var(--blue); }
  .hero-slant {
    position: absolute; inset: 0;
    background: #8b9da1;
    clip-path: polygon(700px 0, 1070px 0, 1070px 590px, 545px 590px);
  }
  .hero-photo {
    position: absolute; inset: 0;
    background: linear-gradient(160deg, var(--photo-light) 0%, var(--photo-dark) 100%);
    clip-path: polygon(738px 0, 1070px 0, 1070px 590px, 600px 590px);
  }
  .hero-title { position: absolute; left: 60px; top: 50px; color: var(--white); font-family: "Montserrat", sans-serif; line-height: 1; }
  .hero-title .light { display: block; font-weight: 300; font-size: 62px; letter-spacing: 1px; }
  .hero-title .bold { display: block; font-weight: 800; font-size: 66px; margin-top: 10px; letter-spacing: 1px; }
  .hero-sub {
    position: absolute; left: 60px; top: 208px; width: 560px; height: 62px;
    background: var(--slate);
    clip-path: polygon(0 0, 100% 0, 96% 100%, 0 100%);
    color: var(--white); font-family: "Montserrat", sans-serif; font-weight: 400;
    font-size: 17px; line-height: 23px; padding: 8px 18px;
  }
  .hero-copy { position: absolute; left: 60px; top: 286px; width: 505px; color: var(--white); font-size: 11.5px; line-height: 15.6px; }
  .hero-copy p + p { margin-top: 10px; }
  .hero-copy p.justify { text-align: justify; }

  /* Testimonials */
  .testimonials {
    position: absolute; left: 640px; top: 540px; width: 375px; height: 465px;
    background: linear-gradient(180deg, #f6f6f7 0%, #ececee 100%);
    padding: 18px 26px 0 28px;
  }
  .testimonial-head { display: flex; align-items: flex-start; gap: 14px; margin-bottom: 10px; }
  .quote-mark { font-family: "Montserrat", sans-serif; font-weight: 800; font-size: 96px; line-height: 80px; height: 56px; color: var(--blue); }
  .testimonial-title { font-family: "Montserrat", sans-serif; font-weight: 400; font-size: 27px; line-height: 30px; color: var(--ink); }
  .testimonial-title b { font-weight: 700; }
  .testimonial { font-size: 11.5px; line-height: 13.6px; text-align: justify; color: var(--ink-soft); }
  .testimonial + .testimonial { margin-top: 12px; }
  .testimonial-group + .testimonial-group { margin-top: 26px; }

  /* Results & services */
  .results-quote {
    position: absolute; left: 60px; top: 598px; width: 545px;
    font-family: "Montserrat", sans-serif; font-style: italic; font-weight: 500;
    font-size: 17.5px; line-height: 23px; color: var(--ink-soft);
  }
  .services-band {
    position: absolute; left: 56px; top: 706px; width: 555px; height: 50px;
    background: var(--slate); color: var(--white);
    font-family: "Montserrat", sans-serif; font-weight: 300; font-size: 38px;
    line-height: 50px; text-align: center; letter-spacing: 0.5px;
    box-shadow: 0 6px 8px rgba(0,0,0,0.15);
  }
  .services-band b { font-weight: 800; }
  .services-list {
    position: absolute; left: 58px; top: 775px; width: 555px;
    display: grid; grid-template-columns: 280px 275px; row-gap: 13px;
    list-style: none;
  }
  .services-list li { display: flex; gap: 8px; font-size: 12.5px; line-height: 16.5px; color: var(--ink-soft); padding-right: 14px; }
  .services-list svg { flex: 0 0 20px; margin-top: 1px; }

  /* Benefits */
  .benefits { position: absolute; left: 48px; top: 1014px; width: 975px; display: flex; justify-content: space-between; }
  .bubble {
    width: 188px; height: 78px; border-radius: 50%;
    display: flex; align-items: center; justify-content: center; text-align: center;
    font-size: 12.5px; line-height: 16.5px; padding: 0 26px;
    box-shadow: 0 10px 10px -6px rgba(0,0,0,0.22);
  }
  .bubble-lead { background: var(--slate); color: var(--white); font-family: "Montserrat", sans-serif; font-weight: 700; font-size: 21px; line-height: 23px; width: 190px; }
  .bubble-grey { background: var(--bubble-light); color: var(--ink); }
  .bubble-blue { background: var(--blue); color: var(--white); }
  .bubble-white { background: var(--bubble-white); color: var(--ink); }
  .bubble-slate { background: var(--slate); color: var(--white); width: 168px; }

  /* Footer */
  .footer {
    position: absolute; left: 0; top: 1110px; width: 1070px; height: 90px;
    background: var(--footer); color: var(--white);
    display: flex; align-items: center; padding: 0 60px;
    font-family: "Montserrat", sans-serif; font-size: 19px; line-height: 25px; letter-spacing: 1px;
  }
  .footer-lead { font-weight: 400; width: 440px; }
  .footer-arrow { margin: 0 26px 0 16px; }
  .footer-contact { font-weight: 700; }
</style>
</head>
<body>
  <header class="hero">
    <div class="hero-slant"></div>
    <div class="hero-photo" role="img" aria-label="Portrait photograph of coach Mirela Hastow standing with arms crossed, wearing a pale pink jacket"></div>
    <h1 class="hero-title"><span class="light">HELPING</span><span class="bold">YOUR CHILD</span></h1>
    <div class="hero-sub">with ADHD or Other Learning<br>Challenges Thrive in College and Beyond</div>
    <div class="hero-copy">
      <p>Academic success coaching that leads to lifelong transformation for students with ADHD and similar challenges that may have impeded their ability to thrive.</p>
      <p>Sending your child off to college can feel scary, especially if that college is hundreds of miles away. You worry about how they’ll do on their own—whether they’ll make friends, earn good grades, and be happy—especially without you there to support them daily. You know your child is bright, and you want them to have a great future, but you’re concerned they will struggle without the right support and resources.</p>
      <p class="justify">You don’t need to feel helpless as you send your child off to this next stage of their lives. Mirela is dedicated to making that transition easier for everyone. Mirela Hastow has years of experience helping students thrive despite their challenges. She sees your child’s potential and helps them see it, too. She provides a safety net as they adjust to a new environment at college. Her services are comprehensive and adaptable, based on the requirements of each individual: helping with course selection and scheduling, time management, study strategies, focus, making new friends, and adapting to change. Through it all, Mirela guides students through fundamental work on mindset to ensure that changes stick.</p>
    </div>
  </header>

  <aside class="testimonials">
    <section class="testimonial-group">
      <div class="testimonial-head">
        <span class="quote-mark">“</span>
        <h2 class="testimonial-title">What<br><b>Parents</b> Say</h2>
      </div>
      <p class="testimonial">“Mirela was the glue that kept our daughter in college… as our daughter’s Academic Coach, [she] gave our daughter the ability to finish strong by empowering her with the skills needed to be successful.”—Lorna</p>
      <p class="testimonial">“Mirela has always told my daughter not that she can succeed, but that she will succeed.”—Maren</p>
    </section>
    <section class="testimonial-group">
      <div class="testimonial-head">
        <span class="quote-mark">“</span>
        <h2 class="testimonial-title">What<br><b>Students</b> Say</h2>
      </div>
      <p class="testimonial">Last semester I completed all 16 hours and I had the highest GPA I’ve ever had!” —Former student</p>
      <p class="testimonial">“Under her instruction, my grades began to improve. I ended up making the Dean’s List during my time at Redfield, and I was also inducted into Tau Kappa Rho. I am currently in my first year of law school at Halbrook University, a top tier school.”—Former student</p>
    </section>
  </aside>

  <p class="results-quote">Mirela has taken students from failing to a 3.0 GPA, and from a C student to the Dean’s List, in just one semester. It doesn’t take years to provide lasting results; all it takes is the right guide.</p>

  <h2 class="services-band">HOW <b>MIRELA</b> HELPS</h2>

  <ul class="services-list">
    <li><svg width="20" height="14" viewBox="0 0 20 14"><path d="M2 1l6 6-6 6M10 1l6 6-6 6" fill="none" stroke="#89abb9" stroke-width="1.3"/></svg><span>Tailors support so that your child improves focus and maximizes their potential in college and beyond.</span></li>
    <li><svg width="20" height="14" viewBox="0 0 20 14"><path d="M2 1l6 6-6 6M10 1l6 6-6 6" fill="none" stroke="#89abb9" stroke-width="1.3"/></svg><span>Understands your child’s unique needs – she sees the gifts that others often miss.</span></li>
    <li><svg width="20" height="14" viewBox="0 0 20 14"><path d="M2 1l6 6-6 6M10 1l6 6-6 6" fill="none" stroke="#89abb9" stroke-width="1.3"/></svg><span>Helps with the logistics of scheduling in a way that most advisors can’t, enrolling students in the courses that best suit their learning style.</span></li>
    <li><svg width="20" height="14" viewBox="0 0 20 14"><path d="M2 1l6 6-6 6M10 1l6 6-6 6" fill="none" stroke="#89abb9" stroke-width="1.3"/></svg><span>Knows the academic landscape intimately, including the challenges faced by students with ADHD and other conditions.</span></li>
    <li><svg width="20" height="14" viewBox="0 0 20 14"><path d="M2 1l6 6-6 6M10 1l6 6-6 6" fill="none" stroke="#89abb9" stroke-width="1.3"/></svg><span>Nurtures the brilliance in your bright child.</span></li>
    <li><svg width="20" height="14" viewBox="0 0 20 14"><path d="M2 1l6 6-6 6M10 1l6 6-6 6" fill="none" stroke="#89abb9" stroke-width="1.3"/></svg><span>Provides a balance between encouraging students and challenging them.</span></li>
  </ul>

  <section class="benefits">
    <div class="bubble bubble-lead">YOU<br>WILL HAVE:</div>
    <div class="bubble bubble-grey">Less stress, knowing that your child is in good hands.</div>
    <div class="bubble bubble-blue">Fewer sleepless nights worrying about your child.</div>
    <div class="bubble bubble-white">Confidence that they are receiving the right support.</div>
    <div class="bubble bubble-slate">Joy and pride at seeing them do well.</div>
  </section>

  <footer class="footer">
    <p class="footer-lead">TO LEARN MORE AND DISCUSS YOUR CHILD’S INDIVIDUAL NEEDS,</p>
    <svg class="footer-arrow" width="22" height="18" viewBox="0 0 22 18"><path d="M2 2l7 7-7 7M11 2l7 7-7 7" fill="none" stroke="#ffffff" stroke-width="1.4"/></svg>
    <p class="footer-contact">CALL 334·555·0148 OR<br>EMAIL COACH@MIRELAHASTOW.EXAMPLE</p>
  </footer>
</body>
</html>
```